CD Cover Design for BRISK TOFFEE

We need a groovy cover design for a new comedy CD called "Brisk Toffee." We have in mind a retro 1960s-70s feel based on the subject material of the CD, but we are open to other ideas.

In the title track, the comedian discusses candy from the past like Rosa Belles, Comet Blazers, Plum Tops, Zippy Tubes, Wax Candies, Candy Cigarettes, Candy Necklaces, etc. These specific candies do not need to be depicted, but we include them here as explanation for the name.

Target Market(s)

Men & Women, ages 25-85, but primarily over 40

Industry/Entity Type

Comedian

Requirements
Must have
• Front & Back Cover designs, both square format
• Front Cover - Title: "Brisk Toffee"
• Back Cover - Photo of Comedian (use one of the photos uploaded)
• Back Cover - Tracks listed as follows:
• 1 – Field Hockey / Parenting
• 2 – Teenagers
• 3 – Parent Teacher Conferences
• 4 – Maine
• 5 – Criminals
• 6 – Over 50
• 7 – Fun Procedure
• 8 – Guardian Donkey
• 9 – Hearthside Weekly
• 10 – 20th Anniversary
• 11 – Not a Nagger
• 12 – Travel
• 13 – Old School / Playground
• 14 – Brisk Toffee
• 15 – Cease & Desist
• 16 – Bra Shopping
• 17 – Craft Mania
• 18 – MRI Questions
• 19 – Vasectomy
Nice to have
• Retro/Vintage feel, 1960s-70s
• Original illustrations of "Brisk Toffee" would be greatly appreciated
Should not have
• Candy hearts with words

```html
<!DOCTYPE html>
<html lang="en">
<head>
<meta charset="utf-8">
<title>Brisk Toffee – CD Cover, Front and Back</title>
<link rel="stylesheet" href="https://fonts.googleapis.com/css2?family=Arimo:wght@700&display=swap">
<style>
  :root {
    --stage: #efe9df;
    --navy: #1f1a5c;
    --ink: #1a1a1a;
    --lemon: #f4ef93;
    --magenta: #e8488f;
    --magenta-deep: #d9327d;
    --candy-red: #e0332f;
    --candy-yellow: #f6d23a;
    --candy-purple: #8a55b8;
    --candy-green: #5cc45a;
    --candy-pink: #f07bb0;
    --photo-hair: #e9cf9a;
    --photo-skin: #f1c7ae;
    --photo-shirt: #7fa3dc;
  }
  * { box-sizing: border-box; margin: 0; padding: 0; }
  html, body {
    width: 1200px;
    height: 900px;
    overflow: hidden;
    background: var(--stage);
    font-family: "Arimo", Arial, sans-serif;
  }
  .spread {
    position: absolute;
    inset: 0;
    display: flex;
    align-items: center;
    justify-content: center;
    gap: 60px;
  }
  .cover {
    position: relative;
    width: 520px;
    height: 520px;
    overflow: hidden;
    box-shadow: 0 6px 18px rgba(0, 0, 0, 0.18);
  }

  /* Front cover */
  .front-art {
    position: absolute;
    inset: 0;
    background:
      radial-gradient(circle at 22% 22%, var(--candy-yellow) 0 16%, transparent 17%),
      radial-gradient(circle at 55% 16%, var(--candy-pink) 0 15%, transparent 16%),
      radial-gradient(circle at 82% 24%, var(--candy-red) 0 19%, transparent 20%),
      radial-gradient(circle at 14% 60%, var(--candy-yellow) 0 12%, transparent 13%),
      radial-gradient(circle at 34% 84%, var(--candy-green) 0 20%, transparent 21%),
      radial-gradient(circle at 84% 80%, var(--candy-purple) 0 20%, transparent 21%),
      radial-gradient(circle at 62% 90%, var(--candy-purple) 0 11%, transparent 12%),
      var(--magenta);
  }
  .front-title {
    position: absolute;
    left: 0;
    right: 0;
    top: 190px;
    text-align: center;
    font-weight: 700;
    font-size: 66px;
    line-height: 1.05;
    letter-spacing: 4px;
    color: var(--navy);
  }

  /* Back cover */
  .back { background: var(--lemon); }
  .back-panel {
    position: absolute;
    inset: 0;
    width: 520px;
    height: 520px;
  }
  .back-photo {
    position: absolute;
    left: 300px;
    top: 90px;
    width: 190px;
    height: 300px;
    border-radius: 90px 90px 40px 40px;
    background: linear-gradient(180deg,
      var(--photo-hair) 0%, var(--photo-skin) 45%, var(--photo-skin) 62%, var(--photo-shirt) 80%, rgba(127,163,220,0) 100%);
  }
  .back-title {
    position: absolute;
    left: 30px;
    top: 26px;
    font-weight: 700;
    font-size: 34px;
    line-height: 1.05;
    letter-spacing: 2px;
    color: var(--navy);
  }
  .track-list {
    position: absolute;
    left: 30px;
    top: 158px;
    list-style: none;
    font-weight: 700;
    font-size: 13px;
    line-height: 17.4px;
    color: var(--ink);
  }
  .track-number {
    display: inline-block;
    min-width: 28px;
  }
</style>
</head>
<body>
<main class="spread">

  <section class="cover front" aria-label="Front cover">
    <div class="front-art" role="img" aria-label="Illustration of grinning, mischievous candy characters in yellow, pink, red, green and purple"></div>
    <h1 class="front-title">BRISK<br>TOFFEE</h1>
  </section>

  <section class="cover back" aria-label="Back cover">
    <svg class="back-panel" viewBox="0 0 520 520" aria-hidden="true">
      <path d="M300 0 C250 140 250 380 360 520 L520 520 L520 0 Z" fill="var(--magenta)"/>
      <path d="M470 0 L520 0 L520 520 L490 520 C505 360 505 160 470 0 Z" fill="var(--magenta-deep)" opacity="0.5"/>
    </svg>
    <div class="back-photo" role="img" aria-label="Portrait photo of the comedian, smiling, in a blue top"></div>
    <h2 class="back-title">BRISK<br>TOFFEE</h2>
    <ol class="track-list">
      <li><span class="track-number">1 –</span> Field Hockey / Parenting</li>
      <li><span class="track-number">2 –</span> Teenagers</li>
      <li><span class="track-number">3 –</span> Parent Teacher Conferences</li>
      <li><span class="track-number">4 –</span> Maine</li>
      <li><span class="track-number">5 –</span> Criminals</li>
      <li><span class="track-number">6 –</span> Over 50</li>
      <li><span class="track-number">7 –</span> Fun Procedure</li>
      <li><span class="track-number">8 –</span> Guardian Donkey</li>
      <li><span class="track-number">9 –</span> Hearthside Weekly</li>
      <li><span class="track-number">10 –</span> 20th Anniversary</li>
      <li><span class="track-number">11 –</span> Not a Nagger</li>
      <li><span class="track-number">12 –</span> Travel</li>
      <li><span class="track-number">13 –</span> Old School / Playground</li>
      <li><span class="track-number">14 –</span> Brisk Toffee</li>
      <li><span class="track-number">15 –</span> Cease &amp; Desist</li>
      <li><span class="track-number">16 –</span> Bra Shopping</li>
      <li><span class="track-number">17 –</span> Craft Mania</li>
      <li><span class="track-number">18 –</span> MRI Questions</li>
      <li><span class="track-number">19 –</span> Vasectomy</li>
    </ol>
  </section>

</main>
</body>
</html>
```